Web Design job - Condo Debts Collection Business needs a Web Design

I need a site for a client, who works with condo debts collection, and ensure all revenues provided by condo fees will be always available to the building manager of condo on a specific date, regardless of defaults.
I have the visual identity (logo, slogan and colors) of the company, and some requirements on layout (kind of slider, menu options, phone number on a noble position, etc) - maybe I can do a sketch, but I like the idea of give some freedom to designer.

*** PLEASE, we have no interest in templates. We want something new***

Target Market(s)

I have two targets for this design: - Condominium's building manager. This target is looking for a solution to overdue debts on it's condo. - Residents on condominiums. This target wants to live in a better place, where their neighbors pay their condominium fees on time.

Number of Pages Required

1 page

Requirements
Must have
• - Slider with title, some short text related, a nice image (I prefer happy and/or peaceful family, people doing business, happy friends, and so on).
• - I have a special attention to menu. I'm looking for one I can have a nice effect, more elegant, charming, kind of innovative.
• - Phone number on the top (or clearly visible).
• - Member log in area or icon on the top (or clearly visible).
• - News/articles area.
• - Modern fonts, with good quality, sans-serif on areas where reading is more intensive (prefer Google web-fonts).
• - Colors specified on attached files.
Nice to have
• - Clear background color, cause it's better to read larger texts (like articles). Dark backgrounds makes reading difficult.
• - A site with effects (like shadows, lines, curves, gradients, lights) is usually pretty.
• - I pay attention on beautiful footers.
Should not have
• - Images with a lot of money (I don't sell richness, I sell tranquility, peace, harmony, safety).
• - Poor menu.

```html
<!DOCTYPE html>
<html lang="en">
<head>
<meta charset="utf-8">
<title>Vestra – Cobrança Condominial</title>
<link rel="stylesheet" href="https://fonts.googleapis.com/css2?family=Montserrat:wght@400;500;600;700&family=Open+Sans:wght@400;600&display=swap">
<style>
:root{
  --gold:#e9a81a;
  --orange:#e8890f;
  --dark:#262626;
  --darker:#1c1c1c;
  --text:#444;
  --muted:#9a9a9a;
  --light:#efefef;
  --white:#fff;
}
*{box-sizing:border-box;margin:0;padding:0}
html,body{width:1200px;height:3696px;overflow:hidden}
body{position:relative;background:var(--white);font-family:"Open Sans",sans-serif;color:var(--text)}
.abs{position:absolute}
.photo{position:absolute}

/* top bar */
.topbar{left:0;top:0;width:1200px;height:32px;background:var(--darker);z-index:3}
.menu{position:absolute;right:86px;top:0;display:flex;gap:30px;height:32px;align-items:center;list-style:none}
.menu li{font:500 12px "Montserrat",sans-serif;color:#d8d8d8;letter-spacing:.5px}

/* hero */
.hero{left:0;top:0;width:1200px;height:665px;background:linear-gradient(100deg,#c9ccd0 0%,#dfe1e3 30%,#b7a89a 60%,#8f8479 100%)}
.brand{left:86px;top:58px;display:flex;align-items:center;gap:12px;z-index:2}
.brand-mark{width:44px;height:44px;background:var(--gold)}
.brand-name{font:700 46px/1 "Montserrat",sans-serif;color:var(--white)}
.brand-tag{left:142px;top:108px;font:600 11px "Montserrat",sans-serif;color:var(--white);letter-spacing:.5px;z-index:2}
.hero-phone{right:86px;top:76px;display:flex;align-items:center;gap:10px;font:500 22px "Montserrat",sans-serif;color:var(--white);z-index:2}
.hero-title{left:86px;top:282px;font:700 42px/1.05 "Montserrat",sans-serif;color:var(--white);text-transform:uppercase}
.btn{display:inline-block;background:var(--gold);color:var(--darker);font:600 15px "Montserrat",sans-serif;letter-spacing:2px;text-transform:uppercase;text-align:center}
.hero-btn{left:86px;top:382px;width:237px;height:42px;line-height:42px}

/* strip */
.strip{left:113px;top:584px;width:974px;height:328px;box-shadow:0 6px 18px rgba(0,0,0,.25)}
.strip-photo{top:0;height:328px}
.strip-middle{left:343px;top:0;width:318px;height:328px;background:#cfc9be}
.strip-card{left:456px;top:601px;width:288px;height:291px;background:#2b2b2b;color:#eee;font-size:13.5px;line-height:22px;text-align:center;padding:52px 26px}

/* intro */
.intro-title{left:0;top:990px;width:1200px;text-align:center;font:600 22px "Montserrat",sans-serif;color:var(--orange)}
.intro-text{left:100px;top:1032px;width:1000px;text-align:center;font-size:12.5px;line-height:24px;color:var(--muted)}

/* features */
.features{left:0;top:1158px;width:1200px;height:313px;background:linear-gradient(180deg,#3a3d43,#4f545a 60%,#3e4146)}
.notch{left:0;top:1136px;width:1200px;height:24px}
.feature{width:200px;text-align:center}
.feature svg{display:block;margin:0 auto}
.feature-label{margin-top:20px;font:600 20px "Montserrat",sans-serif;color:var(--white);text-transform:uppercase}

/* services */
.section-title{left:0;width:1200px;text-align:center;font:600 40px "Montserrat",sans-serif;color:var(--orange);text-transform:uppercase;letter-spacing:1px}
.service-card{background:var(--white);box-shadow:0 4px 20px rgba(0,0,0,.14);padding:40px 44px}
.service-card h3{font:500 21px "Montserrat",sans-serif;color:#222;text-transform:uppercase;letter-spacing:.5px;margin-bottom:14px}
.service-card p{font-size:13px;line-height:22px;color:var(--muted);margin-bottom:20px}
.service-btn{width:166px;height:36px;line-height:36px;font-size:13px}

/* news */
.news{left:0;top:2464px;width:1200px;height:631px;background:var(--light)}
.news-card{background:var(--white);box-shadow:0 2px 8px rgba(0,0,0,.08)}
.featured-tag{left:22px;top:40px;border:1px solid #fff;color:#fff;font:500 13px "Montserrat",sans-serif;padding:3px 10px;letter-spacing:1px}
.featured-title{left:16px;bottom:20px;color:#fff;font:500 22px "Montserrat",sans-serif;text-transform:uppercase}
.news-date{left:10px;top:196px;background:#1f1f1f;color:#eee;font-size:11px;padding:4px 10px}
.news-body{position:absolute;left:18px;top:248px;right:18px}
.news-body h4{font:500 21px "Montserrat",sans-serif;color:#222;text-transform:uppercase;margin-bottom:12px}
.news-body p{font-size:13px;line-height:22px;color:var(--muted)}
.news-body .more{display:block;margin-top:4px;font:700 12px "Montserrat",sans-serif;color:var(--gold);letter-spacing:1px}

/* footer */
.footer{left:0;top:3095px;width:1200px;height:601px;background:linear-gradient(180deg,#2e2e2e,#363636 50%,#252525)}
.footer-brand{left:0;top:3175px;width:1200px;display:flex;justify-content:center;align-items:center;gap:12px}
.footer-tag{left:0;top:3228px;width:1200px;text-align:center;padding-left:56px;font:600 11px "Montserrat",sans-serif;color:var(--white);letter-spacing:.5px}
.footer-lead{left:0;top:3262px;width:1200px;text-align:center;font:400 20px "Montserrat",sans-serif;color:#e6e6e6;letter-spacing:.5px}
.field{background:#ececec;color:#777;font-size:12px;padding:9px 14px}
.send{left:517px;top:3536px;width:166px;height:34px;line-height:34px;font-size:13px}
.footer-line{left:86px;top:3620px;width:1028px;height:1px;background:#4a4a4a}
.footer-info{top:3650px;font-size:13px;color:#bdbdbd;display:flex;align-items:center;gap:8px}
</style>
</head>
<body>

<!-- Hero -->
<div class="abs hero photo" role="img" aria-label="Smiling family relaxing together on a sofa in a bright living room"></div>
<div class="abs topbar">
  <ul class="menu"><li>HOME</li><li>ABOUT US</li><li>SERVICES</li><li>NEWS</li><li>CONTACT US</li></ul>
</div>
<div class="abs brand"><span class="brand-mark"></span><span class="brand-name">Vestra</span></div>
<div class="abs brand-tag">COBRANÇA CONDOMINIAL</div>
<div class="abs hero-phone">
  <svg width="34" height="34" viewBox="0 0 34 34" aria-hidden="true"><circle cx="17" cy="17" r="15" fill="none" stroke="#e9a81a" stroke-width="2"/><path d="M11 10c1-1 2-1 3 0l2 3c.5 1 0 2-1 2.5 1 2 2.5 3.5 4.5 4.5.5-1 1.5-1.5 2.5-1l3 2c1 1 1 2 0 3-2 2-5 1.5-9-2.5S9 12 11 10z" fill="#e9a81a"/></svg>
  (55) 3100.4820
</div>
<div class="abs hero-title">Lorem ipsum is<br>simply dummy</div>
<div class="abs btn hero-btn">Keep in touch</div>

<!-- Strip -->
<div class="abs strip">
  <div class="photo strip-photo" style="left:0;width:343px;background:linear-gradient(180deg,#4f86c6,#9cbde0 40%,#8c6f5c 70%,#5e6b4b)" role="img" aria-label="Modern apartment building under blue sky"></div>
  <div class="abs strip-middle"></div>
  <div class="photo strip-photo" style="left:661px;width:313px;background:linear-gradient(180deg,#2f6fc0,#7aa8da 35%,#c9a673 65%,#5b7a3c)" role="img" aria-label="Residential condominium with green lawn"></div>
</div>
<div class="abs strip-card">Lorem Ipsum is simply dummy text of the printing and typesetting industry. Lorem Ipsum has been the industry's standard dummy text ever since the 1500s, when an unknown printer took a galley of type and scrambled it to make a type specimen book.</div>

<!-- Intro -->
<h2 class="abs intro-title">Lorem Ipsum is simply dummy text of the printing and typesetting industry.</h2>
<p class="abs intro-text">Lorem Ipsum has been the industry's standard dummy text ever since the 1500s, when an unknown printer took a galley of type and scrambled it to make a type specimen book. It has survived not only five centuries, but also the leap into electronic typesetting, remaining essentially unchanged. It was popularised in the 1960s with the release of Letraset sheets containing Lorem Ipsum passages, and more recently with desktop publishing software.</p>

<!-- Features -->
<div class="abs features photo" role="img" aria-label="Apartment buildings at dusk behind a dark overlay"></div>
<svg class="abs notch" viewBox="0 0 1200 24" preserveAspectRatio="none" aria-hidden="true"><polygon points="0,22 560,22 600,0 640,22 1200,22 1200,24 0,24" fill="#3a3d43"/><polyline points="0,22 560,22 600,0 640,22 1200,22" fill="none" stroke="#d9d9d9" stroke-width="2"/></svg>

<div class="abs feature" style="left:104px;top:1238px">
  <svg width="124" height="124" viewBox="0 0 124 124" aria-hidden="true"><circle cx="62" cy="62" r="58" fill="#2d2d2d" stroke="#e9a81a" stroke-width="5"/><g fill="none" stroke="#fff" stroke-width="3"><rect x="40" y="46" width="36" height="40" rx="3"/><rect x="50" y="38" width="34" height="40" rx="3"/><circle cx="67" cy="58" r="7"/></g></svg>
  <div class="feature-label">Lorem ipsum</div>
</div>
<div class="abs feature" style="left:353px;top:1238px">
  <svg width="124" height="124" viewBox="0 0 124 124" aria-hidden="true"><circle cx="62" cy="62" r="58" fill="#2d2d2d" stroke="#e9a81a" stroke-width="5"/><g fill="none" stroke="#fff" stroke-width="3"><rect x="42" y="36" width="24" height="50"/><rect x="66" y="52" width="18" height="34"/><line x1="48" y1="46" x2="60" y2="46"/><line x1="48" y1="56" x2="60" y2="56"/><line x1="48" y1="66" x2="60" y2="66"/><line x1="36" y1="86" x2="90" y2="86"/></g></svg>
  <div class="feature-label">Lorem ipsum</div>
</div>
<div class="abs feature" style="left:602px;top:1238px">
  <svg width="124" height="124" viewBox="0 0 124 124" aria-hidden="true"><circle cx="62" cy="62" r="58" fill="#2d2d2d" stroke="#e9a81a" stroke-width="5"/><g fill="none" stroke="#fff" stroke-width="3"><circle cx="62" cy="48" r="11"/><path d="M40 88c0-14 10-22 22-22s22 8 22 22z"/><rect x="68" y="74" width="20" height="14"/></g></svg>
  <div class="feature-label">Lorem ipsum</div>
</div>
<div class="abs feature" style="left:851px;top:1238px">
  <svg width="124" height="124" viewBox="0 0 124 124" aria-hidden="true"><circle cx="62" cy="62" r="58" fill="#2d2d2d" stroke="#e9a81a" stroke-width="5"/><g fill="none" stroke="#fff" stroke-width="3"><circle cx="62" cy="54" r="17"/><circle cx="62" cy="54" r="9"/><polyline points="52,68 46,90 56,84 60,92 62,72"/><polyline points="72,68 78,90 68,84 64,92 62,72"/></g></svg>
  <div class="feature-label">Lorem ipsum</div>
</div>

<!-- Services -->
<h2 class="abs section-title" style="top:1528px">Our services</h2>

<div class="photo" style="left:148px;top:1607px;width:438px;height:372px;background:linear-gradient(135deg,#d9dde2,#9fb0c2 45%,#5d7894 75%,#c7d2dc)" role="img" aria-label="Businessman in a suit overlaid with city towers"></div>
<div class="abs service-card" style="left:525px;top:1658px;width:527px;height:269px">
  <h3>Condominium's building manager</h3>
  <p>Lorem Ipsum is simply dummy text of the printing and typesetting industry. Lorem Ipsum has been the industry's standard dummy text ever since the 1500s, when an unknown printer took a galley of type and scrambled it.</p>
  <div class="btn service-btn">Read more</div>
</div>

<div class="photo" style="left:613px;top:2021px;width:442px;height:372px;background:linear-gradient(160deg,#8a6c4e,#c8b49a 40%,#e9e1d6 70%,#a7b7cf)" role="img" aria-label="Happy family of three smiling at home"></div>
<div class="abs service-card" style="left:148px;top:2072px;width:525px;height:271px">
  <h3>Residents on condominiums</h3>
  <p>Lorem Ipsum is simply dummy text of the printing and typesetting industry. Lorem Ipsum has been the industry's standard dummy text ever since the 1500s, when an unknown printer took a galley of type and scrambled it.</p>
  <div class="btn service-btn">Read more</div>
</div>

<!-- News -->
<div class="abs news"></div>
<h2 class="abs section-title" style="top:2522px">Latest news</h2>

<div class="abs news-card" style="left:86px;top:2600px;width:380px;height:426px;overflow:hidden">
  <div class="photo" style="left:0;top:0;width:380px;height:426px;background:linear-gradient(180deg,#2c3a6e,#4b5b8e 40%,#2a2f3f 75%,#1d1f26)" role="img" aria-label="Modern residential tower at twilight"></div>
  <div class="abs featured-tag">FEATURED</div>
  <div class="abs featured-title">Lorem ipsum simply dummy</div>
</div>

<div class="abs news-card" style="left:493px;top:2600px;width:295px;height:426px">
  <div class="photo" style="left:0;top:0;width:295px;height:224px;background:linear-gradient(135deg,#e4e6ea,#b9bfc8 50%,#8d96a3)" role="img" aria-label="Person reviewing bills and documents at a desk"></div>
  <div class="abs news-date">18th Jun, 2018</div>
  <div class="news-body">
    <h4>Lorem ipsum simple</h4>
    <p>It is a long established fact that a reader will be distracted by the readable content of a page when looking at its layout.</p>
    <span class="more">READ MORE</span>
  </div>
</div>

<div class="abs news-card" style="left:816px;top:2600px;width:298px;height:426px">
  <div class="photo" style="left:0;top:0;width:298px;height:224px;background:linear-gradient(135deg,#7d5a3e,#c9a27e 45%,#dfe3ea 75%,#a9b4c6)" role="img" aria-label="Hands passing house keys between two people"></div>
  <div class="abs news-date">13th May, 2018</div>
  <div class="news-body">
    <h4>Contrary popular</h4>
    <p>It is a long established fact that a reader will be distracted by the readable content of a page when looking at its layout.</p>
    <span class="more">READ MORE</span>
  </div>
</div>

<!-- Footer -->
<div class="abs footer photo" role="img" aria-label="Tall building facade seen from below, darkened"></div>
<div class="abs footer-brand"><span class="brand-mark"></span><span class="brand-name">Vestra</span></div>
<div class="abs footer-tag">COBRANÇA CONDOMINIAL</div>
<div class="abs footer-lead">Fill this form to contact us:</div>

<div class="abs field" style="left:172px;top:3317px;width:414px;height:35px">Name</div>
<div class="abs field" style="left:611px;top:3317px;width:414px;height:35px">Phone</div>
<div class="abs field" style="left:172px;top:3378px;width:853px;height:35px">Email</div>
<div class="abs field" style="left:172px;top:3442px;width:853px;height:62px">Message</div>
<div class="abs btn send">Send</div>

<div class="abs footer-line"></div>
<div class="abs footer-info" style="left:262px">
  <svg width="14" height="14" viewBox="0 0 34 34" aria-hidden="true"><path d="M6 4c2-2 4-2 6 0l4 6c1 2 0 4-2 5 2 4 5 7 9 9 1-2 3-3 5-2l6 4c2 2 2 4 0 6-4 4-10 3-18-5S2 8 6 4z" fill="#e9a81a"/></svg>
  (55) 3100.4820
</div>
<div class="abs footer-info" style="left:462px;width:280px;justify-content:center">Copyright © 2018 &nbsp;|&nbsp; All Rights Reserved</div>
<div class="abs footer-info" style="left:826px">
  <svg width="14" height="11" viewBox="0 0 14 11" aria-hidden="true"><rect width="14" height="11" fill="#e9a81a"/><polyline points="0,0 7,6 14,0" fill="none" stroke="#333" stroke-width="1.2"/></svg>
  contato@vestra.com.br
</div>

</body>
</html>
```